TRU PEAK POWER.

I'd like my business logo.
contact name: Desmond Halvik
phone:0438275160
email: info@trupeakpower.net.au
website: www.trupeakpower.net.au

services:
solar
battery storage
LED lighting
energy saving solutions
general electrical
I'd like the design to look professional

Target Market(s)

Everyone

Industry/Entity Type

Business

Contact Information for Business Card

as described above

Requirements
Must have
• Id like the colours and the design to work well with my logo.

```html
<!DOCTYPE html>
<html lang="en">
<head>
<meta charset="utf-8">
<title>Tru Peak Power – Business Card</title>
<link rel="stylesheet" href="https://fonts.googleapis.com/css2?family=Montserrat:wght@400;500;700;800&display=swap">
<style>
  :root {
    --green-deep: #279a3f;
    --green: #33ae48;
    --green-light: #8dc63f;
    --gold: #f4a81d;
    --gold-light: #f9c24a;
    --white: #ffffff;
    --paper: #f7f7f5;
    --backdrop: #e9e9e6;
  }
  * { margin: 0; padding: 0; box-sizing: border-box; }
  html, body { width: 1200px; height: 1022px; overflow: hidden; }
  body {
    background: var(--backdrop);
    font-family: "Montserrat", sans-serif;
    position: relative;
  }
  .business-card {
    position: absolute;
    left: 110px;
    top: 231px;
    width: 980px;
    height: 560px;
    border-radius: 28px;
    overflow: hidden;
    background: var(--green);
    box-shadow: 0 18px 40px rgba(0,0,0,0.18);
  }
  .card-shapes { position: absolute; inset: 0; }
  .brand-mark {
    position: absolute;
    left: 80px;
    top: 150px;
    width: 260px;
    height: 260px;
    border-radius: 50%;
    background: radial-gradient(circle at 40% 40%, var(--gold-light), var(--gold) 60%, var(--green-light) 100%);
  }
  .brand-name {
    position: absolute;
    left: 470px;
    top: 58px;
    font-weight: 800;
    font-size: 42px;
    letter-spacing: 1px;
    color: var(--gold);
    line-height: 1;
  }
  .details {
    position: absolute;
    right: 60px;
    top: 150px;
    text-align: right;
    color: var(--white);
  }
  .contact-name {
    font-weight: 700;
    font-size: 30px;
    color: var(--gold);
    margin-bottom: 14px;
  }
  .line {
    display: flex;
    justify-content: flex-end;
    align-items: center;
    gap: 14px;
    font-size: 19px;
    font-weight: 500;
    line-height: 1.7;
  }
  .line svg { width: 16px; height: 16px; flex: none; }
  .services { margin-top: 24px; }
  .services .line::after {
    content: "";
    width: 10px;
    height: 10px;
    margin: 0 3px;
    border-radius: 50%;
    background: var(--gold);
  }
</style>
</head>
<body>
  <div class="business-card">
    <svg class="card-shapes" viewBox="0 0 980 560" preserveAspectRatio="none" aria-hidden="true">
      <path d="M0 0 H330 C470 140 470 400 360 560 H0 Z" fill="var(--green-light)"/>
      <path d="M0 0 H300 C440 140 440 400 330 560 H0 Z" fill="var(--white)"/>
      <path d="M0 0 H290 C428 140 428 400 320 560 H0 Z" fill="var(--paper)"/>
    </svg>

    <div class="brand-mark" role="img" aria-label="Tru Peak Power emblem area"></div>

    <div class="brand-name">TRU PEAK POWER</div>

    <div class="details">
      <div class="contact-name">Desmond Halvik</div>
      <div class="line">0438275160
        <svg viewBox="0 0 16 16"><path d="M4 1 L6.5 4 5 6 Q7 10 10 11 L12 9.5 15 12 13 15 Q4 14 1 3 Z" fill="none" stroke="var(--gold)" stroke-width="1.6"/></svg>
      </div>
      <div class="line">info@trupeakpower.net.au
        <svg viewBox="0 0 16 16"><rect x="1.5" y="3.5" width="13" height="9" fill="none" stroke="var(--gold)" stroke-width="1.6"/><path d="M1.5 3.5 8 9 14.5 3.5" fill="none" stroke="var(--gold)" stroke-width="1.6"/></svg>
      </div>
      <div class="line">www.trupeakpower.net.au
        <svg viewBox="0 0 16 16"><circle cx="8" cy="8" r="6.5" fill="none" stroke="var(--gold)" stroke-width="1.6"/><path d="M1.5 8 H14.5 M8 1.5 C4 5 4 11 8 14.5 C12 11 12 5 8 1.5" fill="none" stroke="var(--gold)" stroke-width="1.4"/></svg>
      </div>

      <div class="services">
        <div class="line">Solar</div>
        <div class="line">Battery storage</div>
        <div class="line">LED lighting</div>
        <div class="line">Energy saving solutions</div>
      </div>
    </div>
  </div>
</body>
</html>
```